Bag cardboard

Hi,

We are a language school, We want to provide our students with a bag cardboard each time they suscribe for a language course.

You can find in the attachement a pictutre of our current model.

For the new one, we want 3 logos to be included. (you can find in the attachement the 3 logos).

We also want our 3 adresses to be included in the model
Tunis - Imm Les Amandiers, 2ème étage 47 Rue du Lac Malawi, 1082 Les Rives du Parc 2
(phone logo) 71 438 617
(Email logo) tunis@parlovia.org

Sfax - Imm Yasmina, 4ème étage Rue Hédi Karray (en face de la poste), 3041 Sfax
(phone logo) 74 512 976
(email logo) sfax@parlovia.org

Sousse - 57 Ave Jules Ferrand (prés du rond point Horizon au dessus du café Mimosa).
(phone logo) 73 658 104
(email logo) sousse@parlovia.org

The website needs to be cited also :
www.parlovia.org

And also the Facebook Page
(Facebook logo) /PARLOVIA

Waiting for your suggestions !

Thx

```html
<!DOCTYPE html>
<html lang="fr">
<head>
<meta charset="utf-8">
<title>Parlovia – sac cartonné</title>
<link rel="stylesheet" href="https://fonts.googleapis.com/css2?family=Source+Sans+3:wght@300;400;600&display=swap">
<style>
  :root{
    --bg:#f3f5f6;
    --paper:#f7f7f6;
    --teal:#0e8f8c;
    --lime:#c8cc12;
    --band-ink:#ffffff;
    --dark:#2a2a2a;
    --brand-lime:#c4c70a;
    --brand-teal:#17898a;
    --brand-olive:#6b6a3a;
    --icon:#e8902a;
  }
  *{box-sizing:border-box;margin:0;padding:0}
  html,body{width:1200px;height:1200px;overflow:hidden;background:var(--bg);
    font-family:"Source Sans 3",Arial,sans-serif}
  .stage{display:flex;gap:40px;justify-content:center;align-items:center;width:1200px;height:1200px}
  .bag{position:relative;width:520px;height:720px;background:var(--paper);display:flex;
    box-shadow:0 10px 30px rgba(0,0,0,.12)}
  .bag--teal{--band:var(--teal)}
  .bag--lime{--band:var(--lime)}
  .contact-band{width:180px;height:100%;background:var(--band);color:var(--band-ink);
    padding:120px 12px 22px 18px;display:flex;flex-direction:column;font-weight:300;font-size:13.5px;line-height:1.3}
  .office{margin-bottom:40px}
  .office__city{font-weight:600}
  .office__address{margin-bottom:8px}
  .office__line{display:flex;align-items:center;gap:7px;margin-top:2px}
  .icon{width:11px;height:11px;flex:none}
  .web{margin-top:auto;font-size:15px;text-align:center}
  .social{display:flex;align-items:center;justify-content:center;gap:6px;font-size:15px;margin-top:4px}
  .social__dot{width:12px;height:12px;border-radius:50%;background:var(--band-ink)}
  .brands{flex:1;display:flex;flex-direction:column;align-items:center;justify-content:space-between;padding:170px 20px 50px}
  .brand{font-weight:600;text-align:center;line-height:1}
  .brand--main{font-size:64px;color:var(--dark)}
  .brand--main-sub{font-size:34px;color:var(--brand-lime);margin-top:4px;text-align:right}
  .brand--lang{font-size:50px;color:var(--brand-teal)}
  .brand--group{font-size:34px;color:var(--brand-olive)}
</style>
</head>
<body>
<main class="stage">
  <article class="bag bag--teal">
    <section class="contact-band">
      <div class="office">
        <p class="office__address"><span class="office__city">Tunis</span> - Imm Les Amandiers, 2ème étage 47 Rue du Lac Malawi, 1082 Les Rives du Parc 2</p>
        <p class="office__line"><svg class="icon" viewBox="0 0 12 12"><circle cx="6" cy="6" r="6" fill="#e8902a"/><path d="M4 3l1.2 1.6-.6.8a4 4 0 002 2l.8-.6L9 8l-.8 1A5 5 0 013 4z" fill="#fff"/></svg>71 438 617</p>
        <p class="office__line"><svg class="icon" viewBox="0 0 12 12"><circle cx="6" cy="6" r="6" fill="#e8902a"/><rect x="3" y="4" width="6" height="4" fill="#fff"/><path d="M3 4l3 2 3-2" stroke="#e8902a" stroke-width=".7" fill="none"/></svg>tunis@parlovia.org</p>
      </div>
      <div class="office">
        <p class="office__address"><span class="office__city">Sfax</span> - Imm Yasmina, 4ème étage Rue des Orangers (en face de la poste), 3041 Sfax</p>
        <p class="office__line"><svg class="icon" viewBox="0 0 12 12"><circle cx="6" cy="6" r="6" fill="#e8902a"/><path d="M4 3l1.2 1.6-.6.8a4 4 0 002 2l.8-.6L9 8l-.8 1A5 5 0 013 4z" fill="#fff"/></svg>74 512 976</p>
        <p class="office__line"><svg class="icon" viewBox="0 0 12 12"><circle cx="6" cy="6" r="6" fill="#e8902a"/><rect x="3" y="4" width="6" height="4" fill="#fff"/><path d="M3 4l3 2 3-2" stroke="#e8902a" stroke-width=".7" fill="none"/></svg>sfax@parlovia.org</p>
      </div>
      <div class="office">
        <p class="office__address"><span class="office__city">Sousse</span> - 57 Ave Jules Ferrand (prés du rond point Horizon au dessus du café Mimosa)</p>
        <p class="office__line"><svg class="icon" viewBox="0 0 12 12"><circle cx="6" cy="6" r="6" fill="#e8902a"/><path d="M4 3l1.2 1.6-.6.8a4 4 0 002 2l.8-.6L9 8l-.8 1A5 5 0 013 4z" fill="#fff"/></svg>73 658 104</p>
        <p class="office__line"><svg class="icon" viewBox="0 0 12 12"><circle cx="6" cy="6" r="6" fill="#e8902a"/><rect x="3" y="4" width="6" height="4" fill="#fff"/><path d="M3 4l3 2 3-2" stroke="#e8902a" stroke-width=".7" fill="none"/></svg>sousse@parlovia.org</p>
      </div>
      <p class="web">www.parlovia.org</p>
      <p class="social"><span class="social__dot"></span>/PARLOVIA</p>
    </section>
    <section class="brands">
      <div><p class="brand brand--main">Parlovia</p><p class="brand brand--main-sub">Centre</p></div>
      <p class="brand brand--lang">LINDORA</p>
      <p class="brand brand--group">TESSAMO</p>
    </section>
  </article>

  <article class="bag bag--lime">
    <section class="contact-band">
      <div class="office">
        <p class="office__address"><span class="office__city">Tunis</span> - Imm Les Amandiers, 2ème étage 47 Rue du Lac Malawi, 1082 Les Rives du Parc 2</p>
        <p class="office__line"><svg class="icon" viewBox="0 0 12 12"><circle cx="6" cy="6" r="6" fill="#e8902a"/><path d="M4 3l1.2 1.6-.6.8a4 4 0 002 2l.8-.6L9 8l-.8 1A5 5 0 013 4z" fill="#fff"/></svg>71 438 617</p>
        <p class="office__line"><svg class="icon" viewBox="0 0 12 12"><circle cx="6" cy="6" r="6" fill="#e8902a"/><rect x="3" y="4" width="6" height="4" fill="#fff"/><path d="M3 4l3 2 3-2" stroke="#e8902a" stroke-width=".7" fill="none"/></svg>tunis@parlovia.org</p>
      </div>
      <div class="office">
        <p class="office__address"><span class="office__city">Sfax</span> - Imm Yasmina, 4ème étage Rue des Orangers (en face de la poste), 3041 Sfax</p>
        <p class="office__line"><svg class="icon" viewBox="0 0 12 12"><circle cx="6" cy="6" r="6" fill="#e8902a"/><path d="M4 3l1.2 1.6-.6.8a4 4 0 002 2l.8-.6L9 8l-.8 1A5 5 0 013 4z" fill="#fff"/></svg>74 512 976</p>
        <p class="office__line"><svg class="icon" viewBox="0 0 12 12"><circle cx="6" cy="6" r="6" fill="#e8902a"/><rect x="3" y="4" width="6" height="4" fill="#fff"/><path d="M3 4l3 2 3-2" stroke="#e8902a" stroke-width=".7" fill="none"/></svg>sfax@parlovia.org</p>
      </div>
      <div class="office">
        <p class="office__address"><span class="office__city">Sousse</span> - 57 Ave Jules Ferrand (prés du rond point Horizon au dessus du café Mimosa)</p>
        <p class="office__line"><svg class="icon" viewBox="0 0 12 12"><circle cx="6" cy="6" r="6" fill="#e8902a"/><path d="M4 3l1.2 1.6-.6.8a4 4 0 002 2l.8-.6L9 8l-.8 1A5 5 0 013 4z" fill="#fff"/></svg>73 658 104</p>
        <p class="office__line"><svg class="icon" viewBox="0 0 12 12"><circle cx="6" cy="6" r="6" fill="#e8902a"/><rect x="3" y="4" width="6" height="4" fill="#fff"/><path d="M3 4l3 2 3-2" stroke="#e8902a" stroke-width=".7" fill="none"/></svg>sousse@parlovia.org</p>
      </div>
      <p class="web">www.parlovia.org</p>
      <p class="social"><span class="social__dot"></span>/PARLOVIA</p>
    </section>
    <section class="brands">
      <div><p class="brand brand--main">Parlovia</p><p class="brand brand--main-sub">Centre</p></div>
      <p class="brand brand--lang">LINDORA</p>
      <p class="brand brand--group">TESSAMO</p>
    </section>
  </article>
</main>
</body>
</html>
```